Luxury Wine Label for New Startup Winery

We need a wine label for our new winery startup. We have worked with a local designer but do not feel the resulting label / logo have the elevation required to present our brand as a luxury wine. Our winery is called "Harrowgate Vineyards" and we are focused on extremely high quality hand crafted artisan and estate wines from the Pacific Northwest.
We would like to see designs that utilize a tree line, or other imagery that represents the "Harrowgate" part of our company name. Another interesting feature could be wood grain.
A logo will be required based on your design so please design with this in mind:
This logo should be consistent with the wine bottle label design, and should be representative of our high end exclusive wine while giving a sense of place (Oregon/ Pacific Northwest.)
I will supply an image of the design we received from our local designer, PLEASE NOTE: in general we do like wood grain and tree line concepts but feel the execution was poorly done.
ATTN: Logo design should be suitable for use on: Bottles (Red wine/rose/white wine), Bussiness cards, vehicle signage, business signage, etc
P.S.:
If you have a design that is not outside the box we are still interested in seeing it.
Label is for a burgundy style bottle with a label height of 3.5 - 4" and a width of 3.5-4"
any label <= 4"x4" and >=3.5"x3.5" will be acceptable:
HOWEVER Width should be greater than or equal to height due to the bottle format
Target Market(s)
Wine enthusiasts with adequate discretionary budgets to afford $100 bottles of wine.
Industry/Entity Type
Wine / Winery
Requirements
Must have
- A sense of luxury, a feel of exclusivity, and a theme consistent with our product and brand name
Nice to have
- Tree line, wood grain or other wood themes. Serif fonts
Should not have
- anything cheesy, off topic, hard to read script fonts or anything that makes the label hard to read from a few feet away or too busy

```html
<!DOCTYPE html>
<html lang="en">
<head>
<meta charset="utf-8">
<title>Harrowgate Vineyards – Syrah Label</title>
<link rel="stylesheet" href="https://fonts.googleapis.com/css2?family=Cormorant+Garamond:wght@500;600&family=Cinzel:wght@500;600&display=swap">
<style>
  :root {
    --page: #ffffff;
    --gold-dark: #a87a2a;
    --gold-mid: #d9b45a;
    --gold-light: #f4dc8e;
    --black: #0a0a0a;
    --charcoal: #1c1d1f;
    --silver-light: #e4e4e6;
    --silver-mid: #a9a9ad;
    --silver-dark: #6f7075;
    --wood-dark: #24130c;
    --wood-mid: #4a2b1c;
    --wood-light: #6a4330;
    --serif: "Cormorant Garamond", Georgia, serif;
    --caps: "Cinzel", Georgia, serif;
  }
  * { margin: 0; padding: 0; box-sizing: border-box; }
  html, body { width: 787px; height: 1200px; overflow: hidden; background: var(--page); }
  .canvas { position: relative; width: 787px; height: 1200px; }

  .front-label {
    position: absolute; left: 96px; top: 50px; width: 595px; height: 484px;
    background: linear-gradient(90deg, var(--black), var(--charcoal) 50%, var(--black));
    overflow: hidden;
  }
  .gold-stripes {
    position: absolute; left: 0; width: 100%; height: 37px;
    background:
      repeating-linear-gradient(180deg, transparent 0 3px, rgba(0,0,0,.75) 3px 4.6px),
      linear-gradient(90deg, var(--gold-dark), var(--gold-light) 30%, var(--gold-dark) 55%, var(--gold-light) 80%, var(--gold-mid));
  }
  .gold-stripes.top { top: 0; }
  .gold-stripes.bottom { bottom: 0; }

  .brand { position: absolute; top: 138px; left: 0; width: 100%; text-align: center; }
  .brand-name {
    font-family: var(--serif); font-weight: 600; font-size: 60px; line-height: 53px;
    letter-spacing: -1px; text-transform: uppercase;
    background: linear-gradient(90deg, var(--silver-dark), var(--silver-light) 45%, var(--silver-dark));
    -webkit-background-clip: text; background-clip: text; color: transparent;
  }
  .region {
    margin-top: 14px; font-family: var(--caps); font-weight: 600; font-size: 16px;
    letter-spacing: 3.5px; color: var(--gold-mid);
  }

  .treeline {
    position: absolute; left: 0; right: 0; top: 350px; height: 97px;
    background:
      linear-gradient(90deg, rgba(168,122,42,.35), rgba(244,220,142,.25) 30%, rgba(168,122,42,.35) 60%, rgba(244,220,142,.25)),
      linear-gradient(180deg, rgba(217,180,90,0) 0%, rgba(217,180,90,.45) 35%, var(--gold-mid) 75%, var(--gold-light));
  }

  .varietal-label {
    position: absolute; left: 96px; top: 554px; width: 595px; height: 130px;
    overflow: hidden;
  }
  .wood-grain {
    position: absolute; inset: 0;
    background:
      radial-gradient(ellipse 120px 40px at 80% 60%, rgba(20,10,6,.55), transparent 70%),
      radial-gradient(ellipse 160px 30px at 25% 35%, rgba(110,70,48,.45), transparent 70%),
      radial-gradient(ellipse 140px 35px at 55% 80%, rgba(20,10,6,.4), transparent 70%),
      linear-gradient(180deg, var(--wood-mid), var(--wood-dark) 45%, var(--wood-mid) 70%, var(--wood-dark)),
      var(--wood-mid);
  }
  .silver-stripes {
    position: absolute; left: 0; width: 100%;
    background:
      repeating-linear-gradient(180deg, transparent 0 2.6px, rgba(30,30,30,.85) 2.6px 3.6px),
      linear-gradient(90deg, var(--silver-dark), var(--silver-light) 40%, var(--silver-mid) 70%, var(--silver-light));
  }
  .silver-stripes.top { top: 0; height: 17px; }
  .silver-stripes.bottom { bottom: 0; height: 15px; }
  .varietal {
    position: absolute; top: 28px; left: 0; width: 100%; text-align: center;
    font-family: var(--serif); font-weight: 600; font-size: 62px; line-height: 60px; letter-spacing: 1px;
    background: linear-gradient(90deg, var(--silver-mid), var(--silver-light) 50%, var(--silver-mid));
    -webkit-background-clip: text; background-clip: text; color: transparent;
  }
  .vintage-tag {
    position: absolute; bottom: 0; left: 207px; width: 181px; height: 15px;
    background: var(--silver-light); text-align: center;
    font-family: var(--serif); font-weight: 600; font-size: 13px; line-height: 15px; color: #3a3a3d;
    font-variant-numeric: lining-nums;
  }
</style>
</head>
<body>
<main class="canvas">
  <section class="front-label">
    <div class="gold-stripes top"></div>
    <div class="brand">
      <h1 class="brand-name">Harrowgate<br>Vineyards</h1>
      <p class="region">WILLAMETTE VALLEY</p>
    </div>
    <div class="treeline" role="img" aria-label="Gold illustration of an evergreen tree line across the label"></div>
    <div class="gold-stripes bottom"></div>
  </section>

  <section class="varietal-label">
    <div class="wood-grain" role="img" aria-label="Dark walnut wood grain texture"></div>
    <div class="silver-stripes top"></div>
    <h2 class="varietal">SYRAH</h2>
    <div class="silver-stripes bottom"></div>
    <p class="vintage-tag">ESTATE | 2023 | GROWN</p>
  </section>
</main>
</body>
</html>
```